Foam Packaging Banner Ad

We are interested in a banner ad design to show a visual reference to our product - expanded polystyrene (EPS) packaging (also known commonly as plumacrest). It should have message components having to do with environmental suitability. If possible, we would prefer an animated graphic design or other 'new' technology (cinemagraph, etc.)

We are a non-profit trade association representing expanded polystyrene manufacturers that make shipping products to protect materials during transportation & delivery. This banner ad is to increase awareness of our website information. We envision a tagline, imagery for the EPS packaging & sustainability and a link to click thru to our website. We have a specific color palette for our branding and can provide other specifications stipulated by the hosting advertisement offer.

To see our website for more details on what we do - www.wavelornguild.org

```html
<!DOCTYPE html>
<html lang="en">
<head>
<meta charset="UTF-8">
<title>Wavelorn Guild – Foam Packaging Banner Set</title>
<link rel="stylesheet" href="https://fonts.googleapis.com/css2?family=PT+Sans:wght@400;700&display=swap">
<style>
  :root {
    --canvas: #e9ebee;
    --white: #ffffff;
    --leaf-deep: #2f6e14;
    --leaf-mid: #5f9c2a;
    --leaf-light: #a9cf5a;
    --curve-green: #3f8a1c;
    --bark: #5a2e1c;
    --gold: #a98a12;
    --ink: #4a2a20;
    --button-top: #e4ef3a;
    --button-bottom: #a9c40f;
    --button-ink: #2b2a10;
    --foam: #e6e8e6;
  }
  * { box-sizing: border-box; margin: 0; padding: 0; }
  html, body { width: 1200px; height: 1200px; overflow: hidden; }
  body {
    background: var(--canvas);
    font-family: "PT Sans", Arial, sans-serif;
    position: relative;
  }
  .banner {
    position: absolute;
    overflow: hidden;
    background: var(--white);
  }
  .banner--skyscraper { left: 300px; top: 98px; width: 211px; height: 788px; }
  .banner--square { left: 606px; top: 571px; width: 380px; height: 315px; }
  .banner--leaderboard { left: 90px; top: 954px; width: 1020px; height: 124px; }

  .banner__backdrop {
    position: absolute;
    background:
      radial-gradient(ellipse at 70% 40%, var(--leaf-light) 0%, transparent 55%),
      linear-gradient(160deg, var(--leaf-mid) 0%, var(--leaf-deep) 70%, #24590f 100%);
  }
  .banner__curve { position: absolute; left: 0; top: 0; width: 100%; height: 100%; }
  .banner__product {
    position: absolute;
    background: linear-gradient(180deg, var(--foam) 0%, #6f9a3a 35%, #3e7a22 60%, var(--foam) 100%);
    border-radius: 4px;
    opacity: 0.9;
  }
  .brand {
    position: absolute;
    display: flex;
    align-items: center;
    gap: 8px;
  }
  .brand__dot {
    border-radius: 50%;
    background: var(--gold);
    flex: none;
  }
  .brand__name {
    color: var(--ink);
    font-weight: 400;
    line-height: 1.05;
  }
  .message { position: absolute; color: var(--white); }
  .message__title { font-weight: 400; line-height: 1; letter-spacing: 0.5px; }
  .message__line { font-weight: 400; line-height: 1.25; }
  .footer-bar { position: absolute; background: var(--bark); }
  .cta {
    position: absolute;
    display: flex;
    align-items: center;
    justify-content: center;
    border-radius: 18px;
    background: linear-gradient(180deg, var(--button-top), var(--button-bottom));
    color: var(--button-ink);
    font-weight: 400;
    text-decoration: none;
    box-shadow: 0 2px 3px rgba(0,0,0,0.35);
  }

  /* skyscraper */
  .banner--skyscraper .banner__backdrop { left: 0; top: 150px; width: 211px; height: 560px; }
  .banner--skyscraper .brand { left: 20px; top: 44px; }
  .banner--skyscraper .brand__dot { width: 76px; height: 76px; }
  .banner--skyscraper .brand__name { font-size: 19px; }
  .banner--skyscraper .banner__product { left: 14px; top: 250px; width: 178px; height: 288px; }
  .banner--skyscraper .message { left: 29px; top: 559px; }
  .banner--skyscraper .message__title { font-size: 39px; margin-bottom: 6px; }
  .banner--skyscraper .message__line { font-size: 20px; }
  .banner--skyscraper .footer-bar { left: 0; top: 694px; width: 211px; height: 94px; }
  .banner--skyscraper .cta { left: 49px; top: 713px; width: 114px; height: 36px; font-size: 17px; }

  /* square */
  .banner--square .banner__backdrop { left: 0; top: 40px; width: 380px; height: 250px; }
  .banner--square .brand { left: 14px; top: 10px; }
  .banner--square .brand__dot { width: 40px; height: 40px; }
  .banner--square .brand__name { font-size: 12px; }
  .banner--square .banner__product { left: 220px; top: 47px; width: 135px; height: 264px; }
  .banner--square .message { left: 28px; top: 134px; }
  .banner--square .message__title { font-size: 37px; margin-bottom: 4px; }
  .banner--square .message__line { font-size: 20px; }
  .banner--square .footer-bar { left: 0; top: 282px; width: 380px; height: 33px; }
  .banner--square .cta { left: 41px; top: 240px; width: 114px; height: 36px; font-size: 17px; }

  /* leaderboard */
  .banner--leaderboard .banner__backdrop { left: 300px; top: 0; width: 480px; height: 124px; }
  .banner--leaderboard .brand { left: 22px; top: 16px; }
  .banner--leaderboard .brand__dot { width: 90px; height: 90px; }
  .banner--leaderboard .brand__name { font-size: 21px; }
  .banner--leaderboard .banner__product { left: 396px; top: 10px; width: 138px; height: 114px; }
  .banner--leaderboard .message { left: 574px; top: 12px; }
  .banner--leaderboard .message__title { font-size: 40px; margin-bottom: 4px; }
  .banner--leaderboard .message__line { font-size: 22px; }
  .banner--leaderboard .footer-bar { left: 779px; top: 0; width: 241px; height: 124px; }
  .banner--leaderboard .cta { left: 842px; top: 44px; width: 122px; height: 38px; font-size: 18px; }
</style>
</head>
<body>

  <section class="banner banner--skyscraper" aria-label="Skyscraper banner">
    <div class="banner__backdrop" role="img" aria-label="Soft green leaf backdrop"></div>
    <svg class="banner__curve" viewBox="0 0 211 788" preserveAspectRatio="none" aria-hidden="true">
      <path d="M0 0 H211 V148 Q110 160 0 190 Z" fill="#ffffff"/>
      <path d="M0 190 Q110 160 211 148 L211 160 Q110 172 0 204 Z" fill="var(--curve-green)"/>
    </svg>
    <div class="brand">
      <span class="brand__dot"></span>
      <span class="brand__name">Wavelorn<br>Guild</span>
    </div>
    <div class="banner__product" role="img" aria-label="Upright vacuum cleaner held in white foam packaging blocks"></div>
    <div class="message">
      <p class="message__title">RECYCLE</p>
      <p class="message__line">YOUR FOAM</p>
      <p class="message__line">PACKAGING HERE</p>
    </div>
    <div class="footer-bar"></div>
    <a class="cta" href="#">CLICK HERE</a>
  </section>

  <section class="banner banner--square" aria-label="Square banner">
    <div class="banner__backdrop" role="img" aria-label="Soft green leaf backdrop"></div>
    <svg class="banner__curve" viewBox="0 0 380 315" preserveAspectRatio="none" aria-hidden="true">
      <path d="M0 0 H380 V10 Q200 30 0 70 Z" fill="#ffffff"/>
      <path d="M0 70 Q200 30 380 10 L380 20 Q200 40 0 80 Z" fill="var(--curve-green)"/>
    </svg>
    <div class="brand">
      <span class="brand__dot"></span>
      <span class="brand__name">Wavelorn<br>Guild</span>
    </div>
    <div class="footer-bar"></div>
    <div class="banner__product" role="img" aria-label="Upright vacuum cleaner held in white foam packaging blocks"></div>
    <div class="message">
      <p class="message__title">RECYCLE</p>
      <p class="message__line">YOUR FOAM</p>
      <p class="message__line">PACKAGING HERE</p>
    </div>
    <a class="cta" href="#">CLICK HERE</a>
  </section>

  <section class="banner banner--leaderboard" aria-label="Leaderboard banner">
    <div class="banner__backdrop" role="img" aria-label="Soft green leaf backdrop"></div>
    <svg class="banner__curve" viewBox="0 0 1020 124" preserveAspectRatio="none" aria-hidden="true">
      <path d="M0 0 H360 Q330 70 300 124 H0 Z" fill="#ffffff"/>
      <path d="M300 124 Q330 70 360 0 H378 Q346 70 314 124 Z" fill="var(--curve-green)"/>
    </svg>
    <div class="brand">
      <span class="brand__dot"></span>
      <span class="brand__name">Wavelorn<br>Guild</span>
    </div>
    <div class="banner__product" role="img" aria-label="Upright vacuum cleaner held in white foam packaging blocks"></div>
    <div class="message">
      <p class="message__title">RECYCLE</p>
      <p class="message__line">YOUR FOAM</p>
      <p class="message__line">PACKAGING HERE</p>
    </div>
    <div class="footer-bar"></div>
    <a class="cta" href="#">CLICK HERE</a>
  </section>

</body>
</html>
```